Dorian "Keep Our Drums Going"

Hello, looking for a flyer design for our band project, we are an Corbin Tribute artist seeking school band programs to work together on a fundraiser where the school band will join our band for 1 night and be part of the show. Red and Black should be the most dominant colors in the flyer. There is a flyer being used by friends of ours for a similar project it can be found at http://www.copperhalltributes.com/wbns.html

the text for the flyer is as follows, again very similar to what the Marigolds guys are using

Dorian Wells - Corbin Tribute Artist presents

"Keep Our Drums Going"

Bring Corbin Tribute Artist - Dorian Wells from Lanternglow Theatre in Maple Hollow, TN to your school to perform with your bands, orchestras, and choirs

Dorian has launched a new fundraising program for schools to keep music programs alive in our schools

What you need to know anout this project

* There is absolutely no cost to the school
* Charts to the Corbin songs will be provided
* Your students perform with Dorian Wells & his band during a special section of the show
* Dorian is available for all local media interviews, and assistance in the promotion of the event on behalf of your program
*A portion of the proceeds are shared with the music program

The concert is educational and entertaining, spanning from the early "bubble gum" years through the Vegas era

Great exposure for your school music program to a whole new audience

Wonderful experience for students that is exciting and FUN!!

_________________

I would prefer this design to be on 8.5 x 11 (if longer page is needed, or front and back is ok also)

please find graphics attached , please feel free to use as few or as many as you would like.

Thanks

```html
<!DOCTYPE html>
<html lang="en">
<head>
<meta charset="utf-8">
<title>Keep Our Drums Going – Flyer</title>
<link href="https://fonts.googleapis.com/css2?family=Alfa+Slab+One&display=swap" rel="stylesheet">
<style>
  :root{
    --red:#d9261c;
    --black:#0b0b0b;
    --white:#ffffff;
    --ink:#1a0c0a;
    --photo-dark:#2a1a16;
    --photo-warm:#8a5a48;
  }
  *{margin:0;padding:0;box-sizing:border-box}
  html,body{width:1200px;height:1000px;overflow:hidden;background:var(--white)}
  .canvas{position:relative;width:1200px;height:1000px;font-family:"Alfa Slab One",Georgia,serif}
  .shapes{position:absolute;inset:0}
  .txt{position:absolute;white-space:nowrap}

  /* front page */
  .front-artist{left:35px;width:532px;top:443px;text-align:center;color:var(--white);font-size:22px;line-height:30px}
  .front-artist .accent{color:var(--red)}
  .front-title{left:80px;top:522px;font-size:33px;line-height:40px;color:var(--ink)}
  .front-title .accent{color:var(--red);margin-left:10px}
  .front-body{left:35px;width:532px;text-align:center;color:var(--white);font-size:13.5px;line-height:18px}
  .front-body.first{top:600px}
  .front-body.second{top:706px}

  /* back page */
  .back-heading{right:442px;top:281px;text-align:right;color:var(--white);font-size:27px;line-height:36px}
  .back-points{left:769px;top:281px;color:var(--red);font-size:14.5px;line-height:19px}
  .back-note{font-size:10.5px;line-height:13px;text-align:center;color:var(--ink)}
  .back-note.era{left:612px;width:248px;top:846px}
  .back-note.exposure{left:628px;width:260px;top:896px}
  .back-fun{left:840px;width:304px;top:877px;text-align:center;color:var(--white);font-size:11.5px;line-height:14px}
</style>
</head>
<body>
<div class="canvas">
  <svg class="shapes" width="1200" height="1000" viewBox="0 0 1200 1000">
    <defs>
      <clipPath id="back-clip"><rect x="612" y="240" width="538" height="696"/></clipPath>
      <radialGradient id="stage-light" cx="50%" cy="40%" r="60%">
        <stop offset="0" stop-color="var(--photo-warm)"/>
        <stop offset="1" stop-color="var(--photo-dark)"/>
      </radialGradient>
    </defs>

    <!-- front page -->
    <rect class="front-page" x="35" y="92" width="532" height="688" fill="var(--black)"/>
    <path class="front-swoosh" fill="var(--red)"
          d="M35,92 L430,92 C470,140 485,230 470,320 C455,400 410,450 370,478 C330,505 285,515 272,535 C262,552 262,568 240,580 C190,600 100,590 35,575 Z"/>
    <circle cx="302" cy="262" r="172" fill="var(--black)"/>
    <circle cx="302" cy="262" r="166" fill="url(#stage-light)" role="img" aria-label="Photo of the tribute artist in a white stage jumpsuit handing a red scarf to a young fan"/>

    <!-- back page -->
    <rect class="back-page" x="612" y="240" width="538" height="696" fill="var(--red)"/>
    <g clip-path="url(#back-clip)">
      <ellipse class="back-swoosh" cx="1010" cy="450" rx="392" ry="300" fill="var(--black)"/>
    </g>
    <circle cx="785" cy="652" r="110" fill="var(--red)"/>
    <circle cx="785" cy="652" r="104" fill="url(#stage-light)" role="img" aria-label="Photo of the tribute artist singing into a microphone"/>
    <circle cx="995" cy="758" r="102" fill="var(--red)"/>
    <circle cx="995" cy="758" r="96" fill="url(#stage-light)" role="img" aria-label="Photo of the tribute artist with arms spread wide on stage"/>
  </svg>

  <!-- front page text -->
  <div class="txt front-artist">Dorian Wells -<br>Corbin Tribute Artist <span class="accent">presents</span></div>
  <div class="txt front-title">"Keep Our<span class="accent">Drums Going"</span></div>
  <div class="txt front-body first">Bring Corbin Tribute Artist - Dorian Wells from<br>Lanternglow Theatre in Maple Hollow, TN to your school<br>to perform with your bands, orchestras, and choirs<br>Dorian has launched a new fundraising program for<br>schools to keep music programs alive in our schools</div>
  <div class="txt front-body second">Dorian has launched a new fundraising program for<br>schools to keep music programs alive in our schools</div>

  <!-- back page text -->
  <div class="txt back-heading">What<br>you<br>need to<br>know<br>anout<br>this<br>project</div>
  <div class="txt back-points">* There is absolutely no cost to the<br>school<br>* Charts to the Corbin songs will be<br>provided<br>* Your students perform with Dorian<br>Wells &amp; his band during a special<br>section of the show<br>* Dorian is available for all local media<br>interviews, and assistance in the<br>promotion of the event on behalf of<br>&nbsp;your program<br>*A portion of the proceeds are<br>shared with the music program</div>
  <div class="txt back-note era">The concert is educational and entertaining,<br>spanning from the early "bubble gum" years<br>through the Vegas era</div>
  <div class="txt back-note exposure">Great exposure for your school music<br>program to a whole new audience</div>
  <div class="txt back-fun">Wonderful experience for students that<br>is exciting and FUN!!</div>
</div>
</body>
</html>
```